Wine Bottle Label Graphic Design (mini bottle 187ml)

Looking for a contemporary custom wine label design for party favors. Inspiration photos provided. **Please see "wine favorite" example in uploads.

Artwork 2.5" wide by 2.75" tall to be placed on 3"x3" stickers. Specs from printer attached but I still want image to fit within the artwork size I specified. Please make label center justified. This is for BOYS. It does not need to be super "masculine"...but definitely not feminine.

Required elements:

Colors: white background, include gold and purple to match logo. Other colors are fine to include.

Name: Toviah 13 (I like use of the No) as shown in the sample, but not required
Varietal: Mitzvah Blend 6.11.2021
Vineyard: Brockel Family Vineyard
Location: Maryland
Logo: See attached (KRNotecard Final)

Serif
Sans Serif

• All the above elements. Clean and crisp design. Contemporary and classy. Purple, Gold, Black colors. See logo. You CAN include cursive font for select elements. I don't mind a combination of print and script.
• Floral, scrolling, background image, old fashioned

```html
<!DOCTYPE html>
<html lang="en">
<head>
<meta charset="utf-8">
<title>Toviah 13 – Mitzvah Blend Label</title>
<link rel="stylesheet" href="https://fonts.googleapis.com/css2?family=Pinyon+Script&family=Playfair+Display:ital,wght@0,700;1,700&family=Old+Standard+TT:wght@400;700&display=swap">
<style>
  :root {
    --backdrop: #ebe9e3;
    --label-white: #fbfbfa;
    --purple: #2e1f6e;
    --gold: #c8973a;
    --ink: #1c1c1c;
  }
  html, body {
    margin: 0;
    padding: 0;
    overflow: hidden;
  }
  .canvas {
    position: relative;
    width: 1200px;
    height: 1200px;
    background: var(--backdrop);
    overflow: hidden;
  }
  .label {
    position: absolute;
    left: 260px;
    top: 70px;
    width: 680px;
    height: 1060px;
  }
  .label-shape {
    position: absolute;
    inset: 0;
  }
  .label-text {
    position: absolute;
    left: 0;
    width: 680px;
    text-align: center;
    margin: 0;
  }
  .couple-name {
    top: 222px;
    font-family: "Old Standard TT", serif;
    font-weight: 700;
    font-size: 22px;
    letter-spacing: 4px;
    color: var(--purple);
  }
  .vineyard {
    top: 375px;
    font-family: "Old Standard TT", serif;
    font-weight: 700;
    font-size: 19px;
    letter-spacing: 0.5px;
    color: var(--ink);
  }
  .wine-name {
    top: 440px;
    font-family: "Pinyon Script", cursive;
    font-size: 92px;
    line-height: 1;
    color: var(--purple);
  }
  .wine-number {
    top: 548px;
    font-family: "Playfair Display", serif;
    font-style: italic;
    font-weight: 700;
    font-size: 118px;
    line-height: 1;
    color: var(--purple);
  }
  .varietal {
    top: 728px;
    font-family: "Old Standard TT", serif;
    font-weight: 700;
    font-size: 27px;
    letter-spacing: 1px;
    transform: scaleX(0.85);
    color: var(--ink);
  }
  .vintage {
    top: 770px;
    font-family: "Old Standard TT", serif;
    font-size: 24px;
    letter-spacing: 10px;
    color: var(--ink);
  }
  .origin-lead {
    top: 868px;
    left: 190px;
    width: auto;
    text-align: left;
    font-family: "Playfair Display", serif;
    font-style: italic;
    font-weight: 700;
    font-size: 15px;
    color: var(--ink);
  }
  .origin-place {
    top: 880px;
    font-family: "Pinyon Script", cursive;
    font-size: 58px;
    line-height: 1;
    color: var(--ink);
  }
</style>
</head>
<body>
<div class="canvas">
  <div class="label">
    <svg class="label-shape" width="680" height="1060" viewBox="0 0 680 1060" xmlns="http://www.w3.org/2000/svg">
      <path d="M0,1040 V280 Q0,190 110,190 H160 A180,180 0 0 1 520,190 H570 Q680,190 680,280 V1040 Z" fill="var(--label-white)"/>
      <path d="M22,1040 V290 Q22,212 112,212 H180 A160,160 0 0 1 500,212 H568 Q658,212 658,290 V1040" fill="none" stroke="var(--gold)" stroke-width="2.5"/>
      <circle cx="340" cy="140" r="62" fill="var(--purple)" stroke="var(--gold)" stroke-width="6"/>
      <line x1="210" y1="706" x2="470" y2="706" stroke="var(--gold)" stroke-width="2.5"/>
      <line x1="232" y1="580" x2="232" y2="640" stroke="var(--gold)" stroke-width="2"/>
      <line x1="448" y1="580" x2="448" y2="640" stroke="var(--gold)" stroke-width="2"/>
      <line x1="22" y1="1010" x2="658" y2="1010" stroke="var(--gold)" stroke-width="2.5"/>
    </svg>
    <p class="label-text couple-name">KIRA AND RONAN</p>
    <p class="label-text vineyard">BROCKEL FAMILY VINEYARD</p>
    <p class="label-text wine-name">Toviah</p>
    <p class="label-text wine-number">13</p>
    <p class="label-text varietal">MITZVAH BLEND</p>
    <p class="label-text vintage">2·0·2·1</p>
    <p class="label-text origin-lead">Made In</p>
    <p class="label-text origin-place">Maryland</p>
  </div>
</div>
</body>
</html>
```